BRTKM Pharma Brochure

Create a BRTKM brochure that targets the pharmaceutical industry using our literature along with vendors literature for the cleanest look.

Bullet points will be

Services:
24/7 Emergency Service
Break Fix
PM Programs
Design Build
In House Electricians and Millwrights
Electrical Trouble Shooting

Products:
ISO Rates Products
High Speed Doors
Sliding Doors
Swinging Doors
Low Energy Closers
Overhead Doors
Loading Dock Equipment
Modular Offices and Rooms
Wepa 10 and 30 Compliant

https://www.vornelsystems.example/en/products/automatic-pedestrian-doors/hermetic-doors/vornel-sabre-kq-kt

```html
<!DOCTYPE html>
<html lang="en">
<head>
<meta charset="utf-8">
<title>BRTKM Pharma Brochure</title>
<link rel="stylesheet" href="https://fonts.googleapis.com/css2?family=Lato:wght@400;700&family=Montserrat:wght@600;700;800&display=swap">
<style>
:root{
  --navy:#3b3d93;
  --navy-dark:#2a2c5c;
  --red:#ec1f27;
  --lavender:#d6daef;
  --ink:#1d1d1f;
  --white:#ffffff;
  --black:#0c0c0c;
}
*{margin:0;padding:0;box-sizing:border-box}
html,body{width:1200px;height:868px;overflow:hidden;background:var(--white)}
.canvas{position:relative;width:1200px;height:868px;background:var(--white);font-family:"Lato",sans-serif;color:var(--ink)}
.page{position:absolute;top:82px;width:545px;height:705px;background:var(--white);overflow:hidden;box-shadow:0 0 3px rgba(0,0,0,.18)}
.page--front{left:42px}
.page--inside{left:614px}

/* front page */
.hero-photo{position:absolute;left:0;top:0;width:545px;height:275px;
  background:linear-gradient(100deg,#e9eef2 0%,#dfe6ec 30%,#c9d3dc 55%,#e6ecf0 75%,#d3dce4 100%)}
.title-band{position:absolute;left:0;top:204px;width:545px;height:71px;
  background:linear-gradient(90deg,rgba(255,255,255,.96) 0%,rgba(255,255,255,.92) 62%,rgba(255,255,255,0) 82%)}
.title-band__bar{position:absolute;left:0;top:0;width:9px;height:71px;background:var(--red)}
.title{position:absolute;left:22px;top:5px;font-family:"Montserrat",sans-serif;font-weight:800;font-size:33px;line-height:31px;color:var(--navy);letter-spacing:.2px;white-space:nowrap}
.title span{color:var(--red)}

.intro{position:absolute;left:22px;top:310px;width:244px;font-size:12.4px;line-height:15px;text-align:justify;color:var(--ink)}
.intro p+p{margin-top:15px}

.services{position:absolute;left:284px;top:296px;width:247px;height:208px;border:1px solid #5b5ca9;
  background:linear-gradient(135deg,#ffffff 40%,#eef0f8 100%)}
.tab{position:absolute;height:28px;display:flex;align-items:center;justify-content:center;white-space:nowrap;
  font-family:"Montserrat",sans-serif;font-weight:700;font-size:16.5px;letter-spacing:.5px;color:var(--white)}
.services .tab{left:27px;top:-1px;width:194px;background:linear-gradient(90deg,var(--navy) 0%,#7a3277 55%,var(--red) 100%)}
.services__list{position:absolute;left:33px;top:47px;list-style:none}
.services__list li{position:relative;padding-left:23px;font-family:"Montserrat",sans-serif;font-weight:700;font-size:12.2px;line-height:14px;color:var(--navy-dark);margin-bottom:7px;letter-spacing:.2px;white-space:nowrap}
.services__list li:nth-child(5){margin-bottom:10px}
.services__list li strong{color:var(--navy);font-weight:700}
.services__list svg{position:absolute;left:0;top:0}

/* inside page */
.side-column{position:absolute;left:350px;top:0;width:195px;height:600px;background:var(--lavender)}
.product-photo{position:absolute;left:365px;width:162px;height:165px;border:1.5px solid var(--navy)}
.product-photo--1{top:13px;background:linear-gradient(180deg,#e8ecf0 0%,#cfd7df 60%,#b9c2cb 100%)}
.product-photo--2{top:187px;background:linear-gradient(180deg,#eef0f2 0%,#d9dde2 55%,#c6ccd2 100%)}
.product-photo--3{top:362px;background:linear-gradient(110deg,#c9d0d6 0%,#9aa6b0 45%,#4fa39a 65%,#cfd6dc 100%)}

.offers .tab{left:75px;top:23px;width:196px;height:30px;background:linear-gradient(90deg,var(--navy) 0%,#8a2f6a 55%,var(--red) 100%)}
.offers__text{position:absolute;left:20px;top:65px;width:307px;font-size:12.4px;line-height:15px;text-align:justify}

.partners{position:absolute;left:13px;top:190px;width:324px;height:45px;border:1.5px solid var(--navy);background:var(--white);
  display:flex;align-items:center;justify-content:space-around;padding:0 6px}
.partner{font-family:"Montserrat",sans-serif;font-weight:700;font-size:16px;letter-spacing:.4px;white-space:nowrap}
.partner--norvale{color:#2a6fb6}
.partner--cleanshield{color:#8ab52b;font-size:13px}
.partner--vornel{color:var(--ink);font-size:19px}

.products{position:absolute;left:13px;top:235px;width:324px;height:269px;
  background:linear-gradient(35deg,var(--red) 0%,#8e2f6e 30%,var(--navy) 62%,var(--navy) 100%)}
.products .tab{left:56px;top:15px;width:195px;height:28px;background:var(--black)}
.products__list{position:absolute;left:28px;top:58px;list-style:none}
.products__list li{position:relative;padding-left:25px;font-family:"Montserrat",sans-serif;font-weight:700;font-size:13.5px;line-height:16px;margin-bottom:5.3px;color:var(--white);letter-spacing:.5px;white-space:nowrap}
.products__list li::before{content:"\221A";position:absolute;left:0;top:0;font-family:"Lato",sans-serif;font-weight:400}

/* footer */
.footer{position:absolute;left:0;top:0;width:545px;height:705px;pointer-events:none}
.footer__shape{position:absolute;left:0;top:0}
.brand-mark{position:absolute;left:197px;top:531px;width:146px;height:72px;background:var(--white);
  display:flex;align-items:center;justify-content:center;text-align:center;
  font-family:"Montserrat",sans-serif;font-weight:800;font-size:19px;line-height:21px;color:var(--red)}
.tagline{position:absolute;left:107px;top:616px;width:330px;height:20px;background:var(--red);color:var(--white);white-space:nowrap;
  font-family:"Montserrat",sans-serif;font-weight:700;font-size:13.5px;letter-spacing:.6px;display:flex;align-items:center;justify-content:center}
.contacts{position:absolute;top:643px;left:13px;right:6px;display:flex;font-size:9.4px;line-height:12px;color:var(--white);white-space:nowrap}
.contacts__col:nth-child(1){width:190px}
.contacts__col:nth-child(2){width:160px}
.web-bar{position:absolute;left:150px;top:686px;width:245px;height:19px;background:var(--black);color:var(--white);white-space:nowrap;
  font-family:"Montserrat",sans-serif;font-weight:700;font-size:12px;letter-spacing:.5px;display:flex;align-items:center;justify-content:center}
</style>
</head>
<body>
<div class="canvas">

  <section class="page page--front">
    <div class="hero-photo" role="img" aria-label="Cleanroom corridor with a technician in protective gear opening a hygienic door"></div>
    <div class="title-band">
      <div class="title-band__bar"></div>
      <h1 class="title">PHARMACEUTICAL<br>DOOR <span>SOLUTION</span></h1>
    </div>

    <div class="intro">
      <p>We are BRTKM Door &amp; Dock Inc and Summit Line Electric, we are comprised of two entities under one roof which allows our customers the satisfaction of knowing that with one phone call many of the everyday problems that occur with plant/ warehouse equipment can be repaired.</p>
      <p>Whether it is a mechanical problem that may require fabricating and welding or an electrical control problem that would require expert troubleshooting, we can fix it.</p>
    </div>

    <div class="services">
      <h2 class="tab">SERVICES</h2>
      <ul class="services__list">
        <li><svg width="16" height="16" viewBox="0 0 16 16"><circle cx="8" cy="8" r="8" fill="#ec1f27"/><path d="M6 4.5 10 8 6 11.5" fill="none" stroke="#fff" stroke-width="2"/></svg><strong>24/7</strong> EMERGENCY SERVICE</li>
        <li><svg width="16" height="16" viewBox="0 0 16 16"><circle cx="8" cy="8" r="8" fill="#ec1f27"/><path d="M6 4.5 10 8 6 11.5" fill="none" stroke="#fff" stroke-width="2"/></svg>BREAK FIX</li>
        <li><svg width="16" height="16" viewBox="0 0 16 16"><circle cx="8" cy="8" r="8" fill="#ec1f27"/><path d="M6 4.5 10 8 6 11.5" fill="none" stroke="#fff" stroke-width="2"/></svg>PM PROGRAMS</li>
        <li><svg width="16" height="16" viewBox="0 0 16 16"><circle cx="8" cy="8" r="8" fill="#ec1f27"/><path d="M6 4.5 10 8 6 11.5" fill="none" stroke="#fff" stroke-width="2"/></svg>DESIGN BUILD</li>
        <li><svg width="16" height="16" viewBox="0 0 16 16"><circle cx="8" cy="8" r="8" fill="#ec1f27"/><path d="M6 4.5 10 8 6 11.5" fill="none" stroke="#fff" stroke-width="2"/></svg>IN HOUSE ELECTRICIANS<br>AND MILLWRIGHTS</li>
        <li><svg width="16" height="16" viewBox="0 0 16 16"><circle cx="8" cy="8" r="8" fill="#ec1f27"/><path d="M6 4.5 10 8 6 11.5" fill="none" stroke="#fff" stroke-width="2"/></svg>ELECTRICAL<br>TROUBLE SHOOTING</li>
      </ul>
    </div>

    <footer class="footer">
      <svg class="footer__shape" width="545" height="705" viewBox="0 0 545 705">
        <polygon points="0,539 272,579 545,539 545,555 272,595 0,555" fill="#ec1f27"/>
        <polygon points="0,555 272,595 545,555 545,705 0,705" fill="#3b3d93"/>
      </svg>
      <div class="brand-mark">BRTKM<br>Door &amp; Dock</div>
      <div class="tagline">SOLUTIONS ★ INTEGRITY ★ RELIABILITY</div>
      <div class="contacts">
        <div class="contacts__col">BRTKM Door &amp; Dock, Inc.<br>Headquarters<br>410 Mercer Ave. Fairview, PA 19000</div>
        <div class="contacts__col">service@brtkm-doors.example<br>estimating@brtkm-doors.example<br>1-800-555-0142</div>
        <div class="contacts__col">BRTKM Door &amp; Dock, NVD<br>North Valley Division<br>725 Orchard Rd. Eastbrook, PA 18000</div>
      </div>
      <div class="web-bar">WWW.BRTKM-DOORS.EXAMPLE</div>
    </footer>
  </section>

  <section class="page page--inside">
    <div class="side-column"></div>
    <div class="product-photo product-photo--1" role="img" aria-label="Automatic hermetic sliding glass door in a hospital corridor"></div>
    <div class="product-photo product-photo--2" role="img" aria-label="High speed roll-up door in a clean production area being washed down"></div>
    <div class="product-photo product-photo--3" role="img" aria-label="Stainless steel hermetic sliding door opening onto an operating room"></div>

    <div class="offers">
      <h2 class="tab">WE OFFERS</h2>
      <p class="offers__text">We offers a full range of products in the entrance-automation sector, combining specialist knowledge with the best known brands. Pharmaceutical Doors is a smart addition to any facility requiring a sterile environment. This tough, hygienic door is completely seamless, eliminating cracks, seams and gaps where bacteria can hide.</p>
    </div>

    <div class="partners">
      <span class="partner partner--norvale">NORVALE</span>
      <span class="partner partner--cleanshield">CLEANSHIELD</span>
      <span class="partner partner--vornel">Vornel</span>
    </div>

    <div class="products">
      <h2 class="tab">PRODUCTS</h2>
      <ul class="products__list">
        <li>ISO RATES PRODUCTS</li>
        <li>HIGH SPEED DOORS</li>
        <li>SLIDING DOORS</li>
        <li>SWINGING DOORS</li>
        <li>LOW ENERGY CLOSERS</li>
        <li>OVERHEAD DOORS</li>
        <li>LOADING DOCK EQUIPMENT</li>
        <li>MODULAR OFFICES AND ROOMS</li>
        <li>WEPA 10 AND 30 COMPLIANT</li>
      </ul>
    </div>

    <footer class="footer">
      <svg class="footer__shape" width="545" height="705" viewBox="0 0 545 705">
        <polygon points="0,539 272,579 545,539 545,555 272,595 0,555" fill="#ec1f27"/>
        <polygon points="0,555 272,595 545,555 545,705 0,705" fill="#3b3d93"/>
      </svg>
      <div class="brand-mark">BRTKM<br>Door &amp; Dock</div>
      <div class="tagline">SOLUTIONS ★ INTEGRITY ★ RELIABILITY</div>
      <div class="contacts">
        <div class="contacts__col">BRTKM Door &amp; Dock, Inc.<br>Headquarters<br>410 Mercer Ave. Fairview, PA 19000</div>
        <div class="contacts__col">service@brtkm-doors.example<br>estimating@brtkm-doors.example<br>1-800-555-0142</div>
        <div class="contacts__col">BRTKM Door &amp; Dock, NVD<br>North Valley Division<br>725 Orchard Rd. Eastbrook, PA 18000</div>
      </div>
      <div class="web-bar">WWW.BRTKM-DOORS.EXAMPLE</div>
    </footer>
  </section>

</div>
</body>
</html>
```